Letterhead for Law Firm Harborcrest Law Group

This would be for virtual letterhead, business cards, etc.

Also logo. I am happy to pay extra for that if it is a separate project.

Harborcrest Law Group

482 Larkmoor Avenue, Suite 730
San Francisco, California 94187

Target Market(s)

Business law services.

Industry/Entity Type

Business

Colors

Designer to choose colors to be used in the design.

```html
<!DOCTYPE html>
<html lang="en">
<head>
<meta charset="utf-8">
<title>Harborcrest Law Group — Letterhead</title>
<link rel="stylesheet" href="https://fonts.googleapis.com/css2?family=Anton&family=Oswald:wght@600&display=swap">
<style>
  :root {
    --paper: #ffffff;
    --ink: #000000;
    --sand: #dfcdab;
  }
  html, body {
    margin: 0;
    padding: 0;
    overflow: hidden;
    background: var(--paper);
  }
  .letterhead {
    position: relative;
    width: 848px;
    height: 1200px;
    overflow: hidden;
    background: var(--paper);
  }
  .letterhead__accent {
    position: absolute;
    inset: 0;
    width: 848px;
    height: 1200px;
  }
  .letterhead__header {
    position: absolute;
    top: 0;
    left: 0;
    width: 848px;
    text-align: center;
    color: var(--ink);
  }
  .firm-name {
    margin: 0;
    padding-top: 6px;
    font-family: "Anton", "Oswald", sans-serif;
    font-weight: 400;
    font-size: 49px;
    line-height: 58px;
    letter-spacing: 0.2px;
  }
  .firm-address {
    margin: 4px 0 0;
    font-family: "Oswald", sans-serif;
    font-weight: 600;
    font-size: 17px;
    line-height: 23px;
    font-style: normal;
    letter-spacing: -0.2px;
  }
</style>
</head>
<body>
  <main class="letterhead">
    <svg class="letterhead__accent" viewBox="0 0 848 1200" aria-hidden="true">
      <polygon class="accent-wedge" points="0,14 838,1200 0,1200" fill="var(--sand)"/>
      <line class="rule rule--header" x1="0" y1="128" x2="848" y2="128" stroke="var(--ink)" stroke-width="2.5"/>
      <line class="rule rule--footer" x1="0" y1="1108" x2="840" y2="1108" stroke="var(--ink)" stroke-width="1.3"/>
    </svg>
    <header class="letterhead__header">
      <h1 class="firm-name">Harborcrest Law Group</h1>
      <address class="firm-address">
        482 Larkmoor Avenue, Suite 730<br>
        San Francisco, California 94187
      </address>
    </header>
  </main>
</body>
</html>
```